Flyer KLV 30 Jahre
Sehr gute Kommunikation. Unser Briefing wurde kreativ und achtsam umgesetzt. Wirklich eine angenehme Zusammenarbeit!
Zielgruppe
Wir begleiten Menschen mit Lernschwierigkeiten, seelischen Behinderungen oder als Familien mit Unterstützungsbedarf zu einer selbstbestimmten Teilhabe am gesellschaftlichen Leben.
Aufgabenstellung
siehe Datei Flyerkonzept

```html
<!DOCTYPE html>
<html lang="de">
<head>
<meta charset="utf-8">
<title>ALDEA e.V. – Flyer</title>
<link href="https://fonts.googleapis.com/css2?family=Open+Sans:wght@400;600;700&display=swap" rel="stylesheet">
<style>
  :root {
    --bg: #c9c8c8;
    --paper: #ffffff;
    --brand-blue: #1f6f8b;
    --band-blue: #176a89;
    --brand-green: #63a766;
    --text-blue: #1d6a8a;
    --photo-light: #e4e4e4;
    --photo-mid: #9a9a9a;
    --photo-dark: #4a4a4a;
    --fold: rgba(0,0,0,.12);
  }
  * { box-sizing: border-box; margin: 0; padding: 0; }
  html, body {
    width: 1200px; height: 800px; overflow: hidden;
    background: var(--bg);
    font-family: "Open Sans", Arial, sans-serif;
  }
  .spread {
    position: absolute; left: 200px; top: 80px;
    width: 800px; height: 640px;
    background: var(--paper);
    box-shadow: 0 20px 40px rgba(0,0,0,.18);
    overflow: hidden;
  }
  .stripe-blue { position: absolute; left: 0; right: 0; top: 0; height: 30px; background: var(--brand-blue); }
  .stripe-green { position: absolute; left: 0; right: 0; top: 30px; height: 24px; background: var(--brand-green); }
  .panel { position: absolute; top: 0; width: 400px; height: 318px; }
  .panel--back { left: 0; }
  .panel--front { left: 400px; }
  .contact {
    position: absolute; left: 0; right: 0; top: 100px;
    text-align: center; color: var(--text-blue); font-style: normal;
    font-size: 15px; line-height: 1.4; letter-spacing: .04em;
  }
  .contact__name { font-weight: 700; margin-bottom: 4px; }
  .contact__group { margin-bottom: 10px; }
  .wordmark {
    position: absolute; left: 0; right: 0; top: 140px;
    display: flex; align-items: center; justify-content: center; gap: 16px;
  }
  .wordmark__dot { width: 22px; height: 22px; border-radius: 50%; background: var(--brand-green); }
  .wordmark__name { font-size: 64px; font-weight: 400; letter-spacing: .08em; color: var(--brand-blue); line-height: 1; }
  .claim-band {
    position: absolute; left: 0; right: 0; top: 318px; height: 42px;
    background: var(--band-blue); display: flex;
  }
  .claim {
    width: 400px; color: #fff; font-size: 20px; letter-spacing: .06em;
    display: flex; align-items: center; justify-content: center;
  }
  .photo {
    position: absolute; left: 0; right: 0; top: 360px; bottom: 0;
    background: linear-gradient(180deg, var(--photo-light) 0%, var(--photo-mid) 55%, var(--photo-dark) 100%);
  }
  .fold { position: absolute; left: 399px; top: 0; bottom: 0; width: 1px; background: var(--fold); }
</style>
</head>
<body>
  <main class="spread">
    <div class="stripe-blue"></div>
    <div class="stripe-green"></div>
    <section class="panel panel--back">
      <address class="contact">
        <p class="contact__name">ALDEA e.V.</p>
        <div class="contact__group">
          <p>Birkenhain-Str. 7</p>
          <p>12049 Berlin</p>
        </div>
        <div class="contact__group">
          <p>Tel.: 030 - 417 203 0</p>
          <p>Fax: 030 - 417 203 29</p>
        </div>
        <div class="contact__group">
          <p>E-Mail: info@aldea-berlin.de</p>
          <p>Web: www.aldea-berlin.de</p>
        </div>
      </address>
    </section>
    <section class="panel panel--front">
      <div class="wordmark">
        <span class="wordmark__dot"></span>
        <span class="wordmark__name">ALDEA</span>
      </div>
    </section>
    <div class="claim-band">
      <p class="claim">Wir begleiten Menschen</p>
      <p class="claim">Wir begleiten Menschen</p>
    </div>
    <div class="photo" role="img" aria-label="Schwarz-Weiß-Foto über beide Seiten: Gruppe junger Erwachsener sitzt lachend an einer Wand, mit Laptop, Kopfhörern und Tablet"></div>
    <div class="fold"></div>
  </main>
</body>
</html>
```